Meridian Handsets business card design

I would like to see some designs for a business card for Meridian Handsets. I would like the business card to be double sided. It will need to have a similar colour / look and feel to our website www.meridianhandsets.com.au I have also attached our latest flyer. Final designs to be handed over in Photoshop format so that I can edit the business card when needed please.

Industry/Entity Type

Business

Contact Information for Business Card

Gavin Thornley
sales@meridianhandsets.com.au
Business Development Manager
ph: (08) 6197 5821
www.meridianhandsets.com.au

Font styles to use
Serif
Sans Serif

Requirements
Must have
• If you could please utilise our colour scheme as seen on our website and the attached flyer.
• I would also like the final design to be in a Photoshop format so that I can edit it when needed please.

```html
<!DOCTYPE html>
<html lang="en">
<head>
<meta charset="utf-8">
<title>Meridian Handsets – Business Card</title>
<link rel="stylesheet" href="https://fonts.googleapis.com/css2?family=Montserrat:wght@600;700&family=Open+Sans:wght@400;600&display=swap">
<style>
  :root {
    --brand-blue: #1b7fc2;
    --charcoal: #333333;
    --ink: #2b2b2b;
    --white: #ffffff;
    --canvas: #e9ebee;
  }
  * { box-sizing: border-box; margin: 0; padding: 0; }
  html, body {
    width: 1200px; height: 900px; overflow: hidden;
    background: var(--canvas);
  }
  .sheet {
    width: 1200px; height: 900px;
    display: flex; flex-direction: column;
    align-items: center; justify-content: center; gap: 40px;
  }
  .card {
    position: relative;
    width: 700px; height: 400px;
    border-radius: 26px;
    overflow: hidden;
    box-shadow: 0 8px 24px rgba(0,0,0,0.18);
  }

  /* Front */
  .card--front { background: var(--white); }
  .front-wordmark {
    position: absolute; left: 0; right: 0; top: 120px;
    text-align: center;
    font-family: "Montserrat", sans-serif; font-weight: 700;
    font-size: 64px; letter-spacing: -0.5px;
    color: var(--brand-blue);
  }
  .front-rule {
    position: absolute; left: 40px; right: 40px; top: 305px;
    height: 2px; background: var(--brand-blue);
  }
  .front-url {
    position: absolute; left: 50%; top: 287px; transform: translateX(-50%);
    background: var(--charcoal);
    padding: 8px 18px;
    font-family: "Open Sans", sans-serif; font-size: 17px;
    color: var(--white); white-space: nowrap;
  }
  .front-url .accent { color: var(--brand-blue); }

  /* Back */
  .card--back { background: var(--brand-blue); }
  .back-band {
    position: absolute; left: 0; right: 0; top: 40px; height: 120px;
    background: var(--charcoal);
  }
  .back-wordmark {
    position: absolute; left: 34px; top: 72px;
    font-family: "Montserrat", sans-serif; font-weight: 600;
    font-size: 46px; color: var(--white);
  }
  .contact {
    position: absolute; left: 410px; top: 220px;
    font-family: "Open Sans", sans-serif; color: var(--ink);
  }
  .contact-name {
    font-family: "Montserrat", sans-serif; font-weight: 700;
    font-size: 25px; line-height: 1.1;
  }
  .contact-name .given { color: var(--white); }
  .contact-name .family { color: var(--ink); }
  .contact-role { font-size: 14px; margin-bottom: 12px; }
  .contact-list { list-style: none; }
  .contact-list li {
    display: flex; align-items: center; gap: 8px;
    font-size: 14.5px; line-height: 1.5; color: var(--white);
  }
  .contact-list svg { width: 12px; height: 12px; flex: none; }
</style>
</head>
<body>
<main class="sheet">

  <section class="card card--front" aria-label="Card front">
    <div class="front-wordmark">Meridian Handsets</div>
    <div class="front-rule"></div>
    <div class="front-url">www.<span class="accent">meridianhandsets</span>.com.au</div>
  </section>

  <section class="card card--back" aria-label="Card back">
    <div class="back-band"></div>
    <div class="back-wordmark">Meridian Handsets</div>

    <div class="contact">
      <p class="contact-name"><span class="given">Gavin</span> <span class="family">Thornley</span></p>
      <p class="contact-role">Business Development Manager</p>
      <ul class="contact-list">
        <li>
          <svg viewBox="0 0 12 12" aria-hidden="true"><path d="M2.5 1 L4.5 1 L5.3 3.4 L4 4.4 Q5 6.8 7.6 8 L8.6 6.7 L11 7.5 L11 9.5 Q10.8 11 9.2 11 Q1 10.4 1 2.6 Q1 1 2.5 1 Z" fill="#2b2b2b"/></svg>
          (08) 6197 5821
        </li>
        <li>
          <svg viewBox="0 0 12 12" aria-hidden="true"><rect x="1" y="2.5" width="10" height="7" fill="none" stroke="#2b2b2b" stroke-width="1.2"/><path d="M1 2.5 L6 6.5 L11 2.5" fill="none" stroke="#2b2b2b" stroke-width="1.2"/></svg>
          sales@meridianhandsets.com.au
        </li>
        <li>
          <svg viewBox="0 0 12 12" aria-hidden="true"><circle cx="6" cy="6" r="5" fill="none" stroke="#2b2b2b" stroke-width="1.1"/><ellipse cx="6" cy="6" rx="2.2" ry="5" fill="none" stroke="#2b2b2b" stroke-width="1"/><path d="M1 6 H11" stroke="#2b2b2b" stroke-width="1"/></svg>
          www.meridianhandsets.com.au
        </li>
      </ul>
    </div>
  </section>

</main>
</body>
</html>
```